The Tideway- All Natural Company Needs Packaging for Main Product

Aloha!

We are a natural products company from Kaua’i, Hawaii called “The Tideway”

The first thing we need packaging for is for our all natural bug spray called “Natural Pest Ward”

We will need much more packaging for many other products in the future so we need a packaging design theme that will serve many products. Our other products are a Reef Safe Sunblock Face Stick called Cheek Shield
Reef Safe Sunblock Body Lotion called Skin Shield and other future natural products.

Very Important:
We love all Sol Pup packaging for its simplicity and cleanness. We honestly want our packaging to be just like Sol Pup in its own way. Instead of having the monkey, we want our Tideway logo to go in the middle like the monkey is on all Sol Pup packaging. We want everything else pretty much the same but just for Bug Spray. Though, we do not want to copy of course, but we would like it be similar.

Front Label- Needs to be on there: (Following guide of Sol Pup Front label)
1. Black Background
2. Tideway logo
3. Make it look professional
4. Make it Clean
5. Make it pop on the shelf
6. Needs to say the following:

** Please not we changed the brief. We changed it so Natural Pest Ward all goes together on the front as one logo for
Natural
Bug
Tideway

a. Natural Pest Ward (where Sol Pup is)
b. Tideway Logo (where monkey is)
c. Deet-Free. (where Golden Blend is)
d. Bug Spray (in between 2 lines) (where Tress Brightener is)
e. Natural Bug Spray enriched (where it says Premium Hair enriched…)
with quality essential oils that
repels mosquitos, gnats, no seeums,
ticks and all other bitey things.
f. Made with Aloha (where it says Blonde to Medium Brown Hair Types)
g. 4 FL OZ/ 118 mL (under Blonde to Medium Brown Hair Types)

Back Label-Things need on there: (Following guide of Sol Pup Back Label)

1. We have given an example Sol Pup Back Label. We would like it to look very similar to it.
2. Make room for a small UPC code on back.
3. Needs to say:

The Tideway products are naturally made for those to enjoy the outdoors.

Reef Safe Gluten Free Hypoallergenic Non-GMO
Deet Free Paraben Free Gluten Free Organic Ingredients

Product Description

Pest Ward is naturally enriched with quality essential oils to repel mosquitos, gnats, no seeums, ticks, and all other bites things. It is safe for babies, kids, and adults.

How to Use

Shake well and spray well on all parts of the body. Reapply every hour while outside.

Warning

Do not spray near or in eyes. If mistakenly sprayed in eyes, rinse with running water for 30 minutes.

Ingredients

Active Ingredients: Cedar wood oil (.35%) Citronella Oil (.30%) Eucalyptus Oil (.20%) Lemongrass Oil (.20%) Lavender Oil (.20%)
Inert Ingredients: Distilled Water, Coconut Oil, Witch Hazel

Exclusively Manufactured and Distributed by The Tideway LLC, 2836 Manuwela Ave. Kilauea, Hawaii, 96812 USA © All Rights Reserved
Get more information at examplepestward.test

Other Notes.
1. The label we’ve been using is 4”x5”
2. The Font we've been using for the Pest Ward logo part is Neutraface but we are glad to try other things that would make it look clean and stand out. Love the Sol Pup logo and font but definitely want something unique for us.

Thank you for all your hard work on this project. Please let us know if you have any questions, and we look forward to seeing your amazing packaging design.

Thanks and Aloha!
The Tideway Team

Target Market(s)

Retail Stores, Adventure Tours, Families

Industry/Entity Type

It Company

Font styles to use
Other font styles liked:
• Professional looking font

Colors
e34196
fbed22
00a990
000000
fbfbfb

Requirements
Must have
• Wrote everything above.
• Must Be VERY professional.
• Clean look.
• POP on a shelf.
• Creative
• White lettering to make it look clean with black background.
Nice to have
• Wrote everything above.
• Must be VERY professional.
• Clean look
• POP on a shelf
• Creative
Should not have
• Clutter
• not look professional
• distractions

```html
<!DOCTYPE html>
<html lang="en">
<head>
<meta charset="utf-8">
<title>Pest Ward – Bug Spray Label</title>
<link rel="stylesheet" href="https://fonts.googleapis.com/css2?family=Oswald:wght@300;400;500;600&family=Playfair+Display:wght@400;600&display=swap">
<style>
  :root {
    --page: #ffffff;
    --label-dark: #151515;
    --label-mid: #2a2a2a;
    --band-light: #6a6a6a;
    --band-dark: #242424;
    --ink: #fbfbfb;
    --ink-soft: #d8d8d8;
    --rule: #cfcfcf;
    --accent: #e34196;
    --stamp-light: #a8a8a8;
    --stamp-dark: #3c3c3c;
  }
  html, body {
    margin: 0;
    padding: 0;
    width: 710px;
    height: 1200px;
    overflow: hidden;
    background: var(--page);
  }
  .label {
    position: absolute;
    left: 215px;
    top: 20px;
    width: 280px;
    height: 1160px;
    background: linear-gradient(90deg, var(--label-mid) 0%, var(--label-dark) 45%, #1e1e1e 100%);
    color: var(--ink);
    text-align: center;
    overflow: hidden;
  }
  .label__band {
    position: absolute;
    left: 0;
    top: 0;
    width: 280px;
    height: 400px;
  }
  .label__natural {
    position: absolute;
    top: 108px;
    width: 100%;
    font-family: "Playfair Display", serif;
    font-size: 17px;
    letter-spacing: 0.5px;
    color: var(--ink);
  }
  .brand {
    position: absolute;
    top: 190px;
    width: 100%;
    display: flex;
    flex-direction: column;
    align-items: center;
    gap: 14px;
  }
  .brand__square {
    width: 40px;
    height: 40px;
    background: var(--accent);
  }
  .brand__name {
    font-family: "Oswald", sans-serif;
    font-weight: 500;
    font-size: 50px;
    line-height: 1;
    color: var(--ink);
    letter-spacing: 1px;
  }
  .stamp {
    position: absolute;
    left: 62px;
    top: 420px;
    width: 167px;
    height: 216px;
    background: linear-gradient(180deg, var(--stamp-light) 0%, #7a7a7a 55%, var(--stamp-dark) 100%);
    outline: 4px dotted #8a8a8a;
    outline-offset: -2px;
  }
  .stamp__place {
    position: absolute;
    left: 12px;
    right: 12px;
    bottom: 10px;
    height: 22px;
    line-height: 22px;
    background: #3a3a3a;
    font-family: "Playfair Display", serif;
    font-size: 13px;
    letter-spacing: 1px;
    color: var(--ink);
  }
  .label__claim {
    position: absolute;
    top: 668px;
    width: 100%;
    font-family: "Playfair Display", serif;
    font-size: 27px;
    color: var(--ink-soft);
  }
  .label__rule {
    position: absolute;
    left: 28px;
    width: 229px;
    height: 1px;
    background: var(--rule);
  }
  .label__rule--top { top: 730px; }
  .label__rule--bottom { top: 800px; }
  .label__product {
    position: absolute;
    top: 734px;
    width: 100%;
    font-family: "Oswald", sans-serif;
    font-weight: 600;
    font-size: 52px;
    line-height: 62px;
    color: var(--ink-soft);
  }
  .label__description {
    position: absolute;
    top: 826px;
    left: 36px;
    width: 208px;
    margin: 0;
    font-family: "Oswald", sans-serif;
    font-weight: 300;
    font-size: 16px;
    line-height: 22px;
    text-align: justify;
    text-align-last: center;
    color: var(--ink-soft);
  }
  .label__footer {
    position: absolute;
    top: 1008px;
    width: 100%;
    font-family: "Oswald", sans-serif;
    font-weight: 300;
    font-size: 17px;
    line-height: 30px;
    color: var(--ink-soft);
  }
  .label__footer p { margin: 0; }
</style>
</head>
<body>
  <main class="label">
    <svg class="label__band" viewBox="0 0 280 400" aria-hidden="true">
      <defs>
        <linearGradient id="band-fill" x1="0" y1="0" x2="1" y2="0.3">
          <stop offset="0" stop-color="var(--band-dark)"/>
          <stop offset="0.55" stop-color="var(--band-light)"/>
          <stop offset="1" stop-color="#4a4a4a"/>
        </linearGradient>
      </defs>
      <polygon points="0,0 280,0 280,300 140,392 0,300" fill="url(#band-fill)"/>
      <polygon points="0,0 280,0 140,52" fill="#1c1c1c" opacity="0.85"/>
      <polygon points="0,60 140,150 280,60 280,70 140,160 0,70" fill="#ffffff" opacity="0.05"/>
    </svg>

    <div class="label__natural">NATURAL</div>

    <div class="brand">
      <div class="brand__square"></div>
      <div class="brand__name">PEST WARD</div>
    </div>

    <div class="stamp" role="img" aria-label="Postage stamp illustration: palm trees over the ocean with a crossed-out bug">
      <div class="stamp__place">★ HAWAII ★</div>
    </div>

    <div class="label__claim">DEET-FREE</div>
    <div class="label__rule label__rule--top"></div>
    <div class="label__product">BUG SPRAY</div>
    <div class="label__rule label__rule--bottom"></div>

    <p class="label__description">Natural Bug Spray enriched with quality essential oils that repels mosquitos, gnats, no seeums, ticks and all other bitey things.</p>

    <div class="label__footer">
      <p>Made with Aloha</p>
      <p>4 FL OZ/ 118 mL</p>
    </div>
  </main>
</body>
</html>
```